Women's Health Company needs business card

We need a business card for a USA based women's health care company. We use digital technology to enhance therapy prescribed by clinicians for their patients

```html
<!DOCTYPE html>
<html lang="en">
<head>
<meta charset="utf-8">
<title>Lumira Health — Business Card</title>
<link rel="stylesheet" href="https://fonts.googleapis.com/css2?family=Roboto:wght@400;500;700&display=swap">
<style>
  :root {
    --purple: #8b4f9e;
    --teal: #6fbfb8;
    --white: #ffffff;
    --paper: #fbfbfb;
    --ink: #2b2b2b;
    --backdrop: #2a2a2c;
  }
  * { margin: 0; padding: 0; box-sizing: border-box; }
  html, body {
    width: 1200px; height: 801px; overflow: hidden;
    background: var(--backdrop);
    font-family: "Roboto", Arial, sans-serif;
  }
  .stage {
    position: relative; width: 1200px; height: 801px;
    display: flex; align-items: center; justify-content: center; gap: 60px;
  }
  .card {
    position: relative; width: 520px; height: 297px; overflow: hidden;
    box-shadow: 0 14px 30px rgba(0,0,0,.45);
  }
  .card-front { background: var(--paper); }
  .card-back { background: var(--purple); }
  .wave { position: absolute; inset: 0; width: 100%; height: 100%; }

  .holder {
    position: absolute; right: 24px; top: 12px; text-align: right;
  }
  .holder-name {
    color: var(--purple); font-weight: 700; font-size: 21px; letter-spacing: .3px; line-height: 1.2;
  }
  .holder-title {
    color: var(--ink); font-size: 13px; line-height: 1.2;
  }

  .contact {
    position: absolute; right: 22px; top: 132px; list-style: none;
    color: var(--white); font-size: 11px; line-height: 1.45; text-align: right;
  }
  .contact li { display: flex; justify-content: flex-end; align-items: center; gap: 7px; }
  .contact .gap { margin-top: 10px; }
  .contact svg { width: 10px; height: 10px; fill: var(--teal); flex: none; }
  .contact .no-icon { padding-right: 17px; }

  .brand {
    position: absolute; display: flex; align-items: center; gap: 8px;
    font-family: "Roboto", Arial, sans-serif; font-weight: 400; white-space: nowrap;
    color: var(--teal);
  }
  .brand-dot { border-radius: 50%; flex: none; }
  .card-front .brand { left: 34px; top: 122px; font-size: 34px; }
  .card-front .brand-dot { width: 9px; height: 9px; background: var(--purple); }
  .card-back .brand { right: 44px; top: 124px; font-size: 44px; }
  .card-back .brand-dot { width: 11px; height: 11px; background: var(--white); }
</style>
</head>
<body>
<main class="stage">

  <section class="card card-front" aria-label="Card front">
    <svg class="wave" viewBox="0 0 520 297" aria-hidden="true">
      <path fill="var(--teal)" d="M520 62 C440 64 376 78 336 124 C296 172 252 266 70 292 L70 297 L520 297 Z"/>
      <path fill="var(--white)" d="M520 70 C446 72 384 86 344 132 C304 180 262 272 84 297 L520 297 Z"/>
      <path fill="var(--purple)" d="M520 74 C452 76 390 92 350 138 C310 186 270 276 100 297 L520 297 Z"/>
    </svg>

    <header class="holder">
      <h1 class="holder-name">MARK ELLISON</h1>
      <p class="holder-title">CEO/Founder</p>
    </header>

    <div class="brand"><span class="brand-dot"></span>Lumira Health</div>

    <ul class="contact">
      <li class="no-icon">Po Box 4120 Street Name</li>
      <li class="no-icon">Country Name CD 2190</li>
      <li class="gap">(123) 555-0142
        <svg viewBox="0 0 10 10"><path d="M2 0.5 L3.8 2.6 L2.9 3.6 Q4 6 6.4 7.1 L7.4 6.2 L9.5 8 L8.3 9.5 Q1.5 8.5 0.5 1.7 Z"/></svg></li>
      <li>(123) 555-0187
        <svg viewBox="0 0 10 10"><path d="M2.5 0 H7.5 V10 H2.5 Z M3.4 1 V8 H6.6 V1 Z" fill-rule="evenodd"/></svg></li>
      <li>info@lumirahealth.com.us
        <svg viewBox="0 0 10 10"><path d="M0 2 H10 V8.5 H0 Z M0.8 2.6 L5 5.8 L9.2 2.6 Z" fill-rule="evenodd"/></svg></li>
      <li>www.lumirahealth.com.us
        <svg viewBox="0 0 10 10"><circle cx="5" cy="5" r="4.6"/></svg></li>
    </ul>
  </section>

  <section class="card card-back" aria-label="Card back">
    <div class="brand"><span class="brand-dot"></span>Lumira Health</div>
  </section>

</main>
</body>
</html>
```